WHAT COMES NEXT? Discovering the reason for being beside the Inner Lamp

Creating a book that is about living a spiritual life. The book is about letting go of the materialistic world and finding happiness through self realisation and enlightenment. The contents page is below that gives an idea of what is contained in the book.

The book is based on the writings of the Sikhs - from India. But it is written in a universal way that is understandable to all.

CONTENTS
Living for a purpose
- Born to be original! Dying as a copy!
- My relationship with everything but me!
- What is my purpose?

Life as a human being!
- Stages of Life
- Five Weaknesses

What is driving our lives?
- Information overload?
- What are your drivers?
- Giving life meaning

You reap what you sow
- Is my destiny written?
- Good and bad actions
- Maya – the illusion and it’s three modes

Slow down and let go
- The mind in overdrive
- Being aware of our mental health
- Why Slow Down?

The Guidance of the Guru
- Why do I need a Guru?
- What the Guru gives you
- Gurbani – the Guru’s Words

Staying connected
- Repeating the Mantra
- Doing two things at once
- Remembering in times of difficulty

Cultivating virtues
- Theory vs Practice
- Virtues and true religion
- Some key virtues

The Mystical Creation
- Experiencing ecstasy
- Enlightenment and intuition
- Spiritual Transformation

Good Company
- How do my companions affect me?
- The company of Saintly people
- Obtaining the fruits that the Guru describes

Serving selflessly
- Serving is our purpose
- Being grateful
- Being generous

Ten things to change your life today

Target Market(s)

All those who want to learn about spirituality. We are targeting young and middle aged but not necessarily ruling out older demographic.

Requirements
Must have
• The book cover:

- exciting and intriguing
- theme is "why am I here" in this world
- some kind of lean towards enlightenment
Nice to have
• It is not essential but the cover could subtly show something about the Sikh faith. Can discuss this further if necessary.
Should not have
• Should not:

- look dull and boring
- don't want it to look like a Buddhism book

```html
<!DOCTYPE html>
<html lang="en">
<head>
<meta charset="utf-8">
<title>What Comes Next? – Book Cover</title>
<link href="https://fonts.googleapis.com/css2?family=Anton&family=Oswald:wght@500;600&family=Cinzel:wght@500&family=Alegreya:wght@400&display=swap" rel="stylesheet">
<style>
  :root{
    --canvas:#ffffff;
    --red-deep:#a50d05;
    --red:#d22a06;
    --orange:#f26a0a;
    --orange-light:#ff9a1f;
    --sun:#fff3b0;
    --gold:#f7d21a;
    --gold-deep:#d69a06;
    --ink:#1a0f08;
    --white:#ffffff;
    --spine:#7e0a04;
  }
  *{margin:0;padding:0;box-sizing:border-box}
  html,body{width:1200px;height:1119px;overflow:hidden;background:var(--canvas)}
  .book-wrap{position:absolute;left:65px;top:110px;width:1070px;height:900px;display:flex}

  /* back cover */
  .back-cover{position:relative;width:520px;height:900px;overflow:hidden;
    background:linear-gradient(160deg,var(--orange) 0%,var(--orange-light) 30%,#e8520a 55%,var(--red) 100%);
    padding:55px 48px 0 52px;color:var(--ink)}
  .back-title{font-family:"Anton",sans-serif;font-size:66px;letter-spacing:1px;text-align:center;
    background:linear-gradient(180deg,#fff6a0,var(--gold) 45%,var(--gold-deep));
    -webkit-background-clip:text;background-clip:text;color:transparent;line-height:1.05}
  .back-rule{height:2px;margin:20px 0 22px;background:linear-gradient(90deg,transparent,#ffe2b0,transparent)}
  .blurb{font-family:"Alegreya",serif;font-size:17.5px;line-height:1.42;text-align:justify}
  .author-note{margin-top:36px;font-family:"Alegreya",serif;font-size:15.5px;line-height:1.45;text-align:justify}
  .author-portrait{float:left;width:92px;height:108px;margin:0 16px 6px 0;border:1px solid #ffd7b0;border-radius:50%}

  /* spine */
  .spine{width:30px;height:900px;background:linear-gradient(90deg,#5e0603,var(--spine) 50%,#5e0603);
    display:flex;flex-direction:column;align-items:center;padding:40px 0 30px;gap:150px}
  .spine-text{writing-mode:vertical-rl;white-space:nowrap}
  .spine-author{font-family:"Cinzel",serif;font-size:15px;color:var(--ink);color:#1a0503}
  .spine-title{font-family:"Anton",sans-serif;font-size:17px;letter-spacing:3px;color:var(--gold)}
  .spine-sub{font-family:"Oswald",sans-serif;font-size:10px;color:var(--white);margin-top:-130px}

  /* front cover */
  .front-cover{position:relative;width:520px;height:900px;overflow:hidden;
    background:radial-gradient(ellipse 70% 45% at 55% 22%,var(--sun) 0%,var(--orange-light) 22%,var(--orange) 45%,var(--red) 75%,var(--red-deep) 100%)}
  .globe{position:absolute;left:105px;top:170px;width:320px;height:320px;border-radius:50%;
    background:radial-gradient(circle at 45% 30%,#ffe680 0%,#f6a321 40%,#c9520a 80%,#9e2e05 100%);opacity:.9}
  .front-title{position:absolute;left:0;right:0;top:48px;text-align:center;
    font-family:"Anton",sans-serif;font-size:168px;line-height:.98;letter-spacing:2px;
    color:rgba(255,110,20,.55);-webkit-text-stroke:3px var(--white)}
  .front-rule{position:absolute;left:100px;right:90px;top:650px;height:3px;
    background:linear-gradient(90deg,transparent,#ffb38a 25%,#ffd9c4 60%,transparent)}
  .subtitle{position:absolute;left:50px;right:40px;top:668px;text-align:center;
    font-family:"Oswald",sans-serif;font-weight:600;font-size:31px;line-height:1.2;color:var(--white)}
  .author-band{position:absolute;left:0;right:0;bottom:0;height:92px;
    background:linear-gradient(90deg,#e7b208,var(--gold) 35%,#f9e03c 60%,var(--gold-deep));
    display:flex;align-items:center;justify-content:center}
  .author-name{font-family:"Cinzel",serif;font-weight:500;font-size:46px;color:var(--ink);letter-spacing:1px}
</style>
</head>
<body>
  <div class="book-wrap">
    <section class="back-cover">
      <h2 class="back-title">WHAT COMES NEXT?</h2>
      <div class="back-rule"></div>
      <p class="blurb">This book seeks the answer to this and other questions about our true identity, what drives us and where we are going. By looking into the Words of the True Guru, called Gurbani, you will gain a different perspective on life and your attitude towards it. The Guru's universal message helps us rise above two significant limitations - attachment to the world and the unfulfilled desires for the things that we want. Only then can we overcome our barriers to discover a life that is rewarding and without limits. We begin by remaining connected to the Creator and serving the creation. With searching questions the book ends with ten things that you can implement today on your journey to self-realisation.</p>
      <div class="author-note">
        <div class="author-portrait" role="img" aria-label="Author portrait"></div>
        Lorem ipsum dolor sit amet, consectetur adipiscing elit, sed do eiusmod tempor incididunt ut labore et dolore magna aliqua. Eu ultrices vitae auctor eu augue ut ullamcorper a lacus vestibulum sed arcu non odio convallis aenean et tortor at risus viverra. Laoreet suspendisse interdum consectetur libero id faucibus nisl tincidunt eget. Integer eget aliquet nibh praesent. Senectus et netus et malesuada fames ac turpis egestas nunc lobortis mattis aliquam faucibus purus in massa scelerisque varius morbi enim nunc. Massa tincidunt dui ut turpis tincidunt id. Vel risus commodo viverra maecenas.
      </div>
    </section>

    <aside class="spine">
      <span class="spine-text spine-author">DALJIT ARORA</span>
      <span class="spine-text spine-title">WHAT COMES NEXT?</span>
      <span class="spine-text spine-sub">Discovering the reason for being beside the Inner Lamp</span>
    </aside>

    <section class="front-cover">
      <div class="globe" role="img" aria-label="Glowing globe of the Earth lit by a radiant sunburst"></div>
      <h1 class="front-title">WHAT<br>COMES<br>NEXT?</h1>
      <div class="front-rule"></div>
      <p class="subtitle">Discovering the reason for being beside the Inner Lamp</p>
      <div class="author-band"><span class="author-name">DALJIT ARORA</span></div>
    </section>
  </div>
</body>
</html>
```